An innovative software company needs a business card!

We need a business card design for our new innovative software company. Please use the details for the business card provided in business card details section. We will use the business card paper like: https://www.plavex.com/us/products/nfc/business-cards-plus.html Our company name: kelvora We have already a logo and colors to use in business cards too ,

Target Market(s)

App & Sofware Development

Industry/Entity Type

Software

Contact Information for Business Card

Lukas Brenner, BSc.
Owner and Creative Superhero

Adress:
Tulpenweg 37/4/1809
A - 1100, Wien

Tel: +43 (0) 676 921 35 60
Email: lukas.brenner@kelvora.at
Web: www.kelvora.at

Requirements
Must have
• - Use our logo
Nice to have
• It would be nice to have a nice picture on the backside. (About apps, software, technicals or funy stuff) - Use our colors as in business card (optional)

```html
<!DOCTYPE html>
<html lang="en">
<head>
<meta charset="utf-8">
<title>kelvora business card</title>
<link rel="stylesheet" href="https://fonts.googleapis.com/css2?family=Oswald:wght@300;400;500&display=swap">
<style>
  :root {
    --stage: #3f3630;
    --brand-blue: #16a3d0;
    --card-white: #ffffff;
    --text-grey: #55585c;
    --rule-blue: #4fbde0;
  }
  * { box-sizing: border-box; margin: 0; padding: 0; }
  html, body {
    width: 1200px;
    height: 1200px;
    overflow: hidden;
    background: var(--stage);
    font-family: "Oswald", sans-serif;
  }
  .canvas { position: relative; width: 1200px; height: 1200px; }
  .card {
    position: absolute;
    width: 700px;
    height: 400px;
    overflow: hidden;
    box-shadow: 0 10px 30px rgba(0,0,0,0.35);
  }
  .card-front { left: 110px; top: 140px; background: var(--brand-blue); }
  .card-back  { left: 390px; top: 650px; background: var(--card-white); }

  .wordmark {
    font-family: "Oswald", sans-serif;
    font-weight: 500;
    letter-spacing: 1px;
    line-height: 1;
  }
  .front-wordmark {
    position: absolute;
    right: 48px;
    bottom: 60px;
    font-size: 110px;
    color: var(--card-white);
  }

  .holder { position: absolute; left: 56px; top: 50px; }
  .holder-name {
    font-size: 44px;
    font-weight: 400;
    letter-spacing: 2px;
    color: var(--brand-blue);
    text-transform: uppercase;
    line-height: 1.1;
  }
  .holder-role {
    font-size: 19px;
    font-weight: 300;
    color: var(--text-grey);
    margin-top: 4px;
  }

  .details {
    position: absolute;
    left: 56px;
    top: 175px;
    display: flex;
    gap: 20px;
    font-size: 19px;
    font-weight: 300;
    color: var(--text-grey);
    line-height: 1.35;
    white-space: nowrap;
  }
  .contact-list { list-style: none; }
  .contact-label { color: var(--brand-blue); font-weight: 400; margin-right: 6px; }
  .details-divider { width: 1px; background: var(--rule-blue); }
  .address { font-style: normal; }

  .rule {
    position: absolute;
    left: 56px;
    right: 56px;
    top: 285px;
    height: 1px;
    background: var(--rule-blue);
  }

  .brand-row {
    position: absolute;
    left: 56px;
    bottom: 26px;
    display: flex;
    align-items: center;
    gap: 18px;
  }
  .brand-dot {
    width: 60px;
    height: 60px;
    border-radius: 50%;
    background: var(--brand-blue);
  }
  .back-wordmark { font-size: 76px; color: var(--brand-blue); }
</style>
</head>
<body>
<main class="canvas">
  <section class="card card-front" aria-label="Card front">
    <div class="wordmark front-wordmark">kelvora</div>
  </section>

  <section class="card card-back" aria-label="Card back">
    <div class="holder">
      <h1 class="holder-name">Lukas Brenner, BSc.</h1>
      <p class="holder-role">Owner and Creative Superhero</p>
    </div>

    <div class="details">
      <ul class="contact-list">
        <li><span class="contact-label">T :</span>+43 (0) 676 921 35 60</li>
        <li><span class="contact-label">E :</span>lukas.brenner@kelvora.at</li>
        <li><span class="contact-label">W:</span>www.kelvora.at</li>
      </ul>
      <div class="details-divider"></div>
      <address class="address">
        Tulpenweg 37/4/1809<br>
        A - 1100, Wien
      </address>
    </div>

    <div class="rule"></div>

    <div class="brand-row">
      <span class="brand-dot"></span>
      <span class="wordmark back-wordmark">kelvora</span>
    </div>
  </section>
</main>
</body>
</html>
```